Business Card Design

I am an independent chairman and director and work a lot in transformation/change and leadership environments. I work for both the New Zealand government and private companies in these capacities.
I've uploaded a basic graphic as a starting point - it is the Fibonacci sequence represented by the growth spiral. The numbers on the back of the card are the actual sequence.
As an idea the background could be gloss purple and the lettering raised print in bright silver.

Industry/Entity Type

Leadership

Contact Information for Business Card

Front
Dalton K. Pryce
Christchurch
New Zealand
dkpryce@fernlo.co.nz

Mob.027.394.861
On Linkvale

Back
Centered 1-1-2-3-5-8-13-21-34-55-89-144-233-377-610-987-1597

```html
<!DOCTYPE html>
<html lang="en">
<head>
<meta charset="utf-8">
<title>Dalton K. Pryce — Business Card</title>
<link rel="stylesheet" href="https://fonts.googleapis.com/css2?family=Noto+Sans:wght@400;700&display=swap">
<style>
  :root {
    --page-bg: #e9e6ec;
    --purple-deep: #9a1fc9;
    --purple-mid: #b325d6;
    --magenta: #d92fd9;
    --wave-light: rgba(255, 255, 255, 0.16);
    --silver: #eeeef2;
    --silver-shade: rgba(60, 0, 80, 0.55);
    --line: #dcdadf;
    --spiral-tint-a: rgba(255, 255, 255, 0.10);
    --spiral-tint-b: rgba(255, 255, 255, 0.03);
  }
  html, body {
    margin: 0;
    padding: 0;
    width: 1108px;
    height: 1200px;
    overflow: hidden;
    background: var(--page-bg);
    font-family: "Noto Sans", sans-serif;
  }
  .canvas {
    position: relative;
    width: 1108px;
    height: 1200px;
  }
  .card {
    position: absolute;
    left: 74px;
    width: 960px;
    height: 540px;
    overflow: hidden;
    background: linear-gradient(115deg, var(--purple-deep) 0%, var(--purple-mid) 55%, var(--magenta) 100%);
    box-shadow: 0 6px 18px rgba(50, 0, 70, 0.25);
  }
  .card--front { top: 40px; }
  .card--back { top: 620px; }
  .card__art {
    position: absolute;
    inset: 0;
    width: 960px;
    height: 540px;
  }
  .spiral-area {
    position: absolute;
    left: 130px;
    top: 20px;
    width: 809px;
    height: 500px;
    background: radial-gradient(ellipse at 72% 62%, var(--spiral-tint-a) 0%, var(--spiral-tint-b) 70%);
  }
  .silver {
    color: var(--silver);
    text-shadow: 1px 1px 0 var(--silver-shade), -1px -1px 0 rgba(255,255,255,0.35);
  }
  .identity {
    position: absolute;
    right: 350px;
    top: 300px;
    text-align: right;
  }
  .identity__name {
    margin: 0;
    font-size: 40px;
    font-weight: 700;
    letter-spacing: 0.5px;
  }
  .identity__city {
    margin: 14px 0 0;
    font-size: 30px;
    font-weight: 700;
    line-height: 32px;
  }
  .identity__email {
    margin: 22px 0 0;
    font-size: 24px;
    font-weight: 400;
  }
  .contact {
    position: absolute;
    left: 650px;
    top: 210px;
    font-size: 24px;
    line-height: 34px;
  }
  .contact p { margin: 0; }
  .sequence {
    position: absolute;
    left: 0;
    right: 0;
    top: 252px;
    margin: 0;
    text-align: center;
    font-size: 25px;
    letter-spacing: 0.2px;
  }
</style>
</head>
<body>
<main class="canvas">

  <section class="card card--front" aria-label="Card front">
    <svg class="card__art" viewBox="0 0 960 540" aria-hidden="true">
      <path d="M0 110 C160 60 300 200 460 170 C620 140 760 60 960 90 L960 0 L0 0 Z" fill="var(--wave-light)"/>
      <rect x="14" y="14" width="932" height="512" fill="none" stroke="var(--line)" stroke-width="2"/>
    </svg>

    <div class="spiral-area" role="img" aria-label="Client-supplied Fibonacci growth spiral drawn over golden rectangles"></div>

    <div class="contact silver">
      <p>Mob.027.394.861</p>
      <p>On Linkvale</p>
    </div>

    <div class="identity silver">
      <h1 class="identity__name">Dalton K. Pryce</h1>
      <p class="identity__city">Christchurch<br>New Zealand</p>
      <p class="identity__email">dkpryce@fernlo.co.nz</p>
    </div>
  </section>

  <section class="card card--back" aria-label="Card back">
    <svg class="card__art" viewBox="0 0 960 540" aria-hidden="true">
      <path d="M0 200 C180 190 320 130 480 90 C640 50 760 40 960 60 L960 0 L0 0 Z" fill="var(--wave-light)"/>
      <path d="M0 470 C200 480 420 420 560 400 C660 386 700 430 760 440 C840 452 900 440 960 430 L960 540 L0 540 Z" fill="var(--wave-light)"/>
    </svg>
    <p class="sequence silver">1-1-2-3-5-8-13-21-34-55-89-144-233-377-610-987-1597</p>
  </section>

</main>
</body>
</html>
```